Box and label design for oil Tincture bottle

I need to design an attractive looking label for a 30ml CBD oil tincture along with designing a box for the tincture oil. I already have the logo (see attachment). I just need a nice, attractive looking artwork for the label and the box. The box is the standard 30ml tincture oil (see example attachment). The box has a total of 6 sides (4 on sides and 2 for top and bottom). Please include a section for supplemental facts and ingredients. Let's not focus to much on content. I am more concerned with design of box and label.
Target Market(s)
CBD customers
Look and feel
Each slider illustrates characteristics of the customer's brand and the style your logo design should communicate.

```html
<!DOCTYPE html>
<html lang="en">
<head>
<meta charset="utf-8">
<title>Calm Harbor CBD – Tincture Box Dieline and Bottle Label</title>
<link rel="stylesheet" href="https://fonts.googleapis.com/css2?family=Montserrat:wght@800&family=Open+Sans:wght@400;600&family=Oswald:wght@600&family=Yellowtail&family=Arimo:wght@700&display=swap">
<style>
  :root {
    --ink: #031a26;
    --gold: #f5c400;
    --navy: #0d2a8a;
    --blue: #0a5cf5;
    --white: #ffffff;
    --rule: #d8ecf5;
    --frame-grey: #6b6f72;
    --script-grey: #c9ccce;
    --tag-deep: #1b6a98;
    --tag-light: #5ab8ee;
    --dieline: #111111;
  }
  * { box-sizing: border-box; margin: 0; padding: 0; }
  html, body { width: 1026px; height: 1200px; overflow: hidden; background: var(--white); }
  .canvas { position: relative; width: 1026px; height: 1200px; overflow: hidden; background: var(--white); }

  .dieline { position: absolute; left: 0; top: 0; width: 1026px; height: 1200px; }

  .panel { position: absolute; background: var(--ink); width: 183px; height: 304.5px; top: 255.5px; }
  .panel--front { left: 175px; }
  .panel--back { left: 358px; }
  .panel--front-b { left: 540.5px; }
  .panel--back-b { left: 723.5px; }
  .panel--top { left: 358px; top: 72px; height: 183.5px; }
  .panel--bottom { left: 540.5px; top: 560px; height: 184px; border: 1px solid var(--dieline); }

  .brand-band {
    position: absolute; left: 0; top: 25px; width: 100%; height: 83px;
    background: var(--white);
    border-top: 2px solid #8a8d90; border-bottom: 2px solid #8a8d90;
  }
  .brand {
    position: absolute; left: 0; width: 100%;
    display: flex; flex-direction: column; align-items: center;
  }
  .brand__circle { width: 42px; height: 42px; border-radius: 50%; border: 2px solid currentColor; }
  .brand__name {
    margin-top: 6px;
    font-family: "Oswald", sans-serif; font-weight: 600; font-size: 16px; line-height: 1;
    letter-spacing: 0.2px; white-space: nowrap;
  }
  .brand--navy { color: var(--navy); }
  .brand--white { color: var(--white); }
  .brand--blue { color: var(--blue); }
  .brand-band .brand { top: 6px; }

  .strength {
    position: absolute; left: 50%; transform: translateX(-50%);
    width: 155px; text-align: center; color: var(--white);
  }
  .strength__frame {
    border: 1px solid var(--rule); border-bottom: none;
    padding-top: 3px; height: 60px;
  }
  .strength__title {
    font-family: "Montserrat", sans-serif; font-weight: 800;
    font-size: 31px; line-height: 1; color: var(--gold); letter-spacing: 0.5px;
    white-space: nowrap;
  }
  .strength__dose {
    font-family: "Open Sans", sans-serif; font-size: 13px; line-height: 1;
    margin-top: 1px; white-space: nowrap;
  }
  .strength__foot { display: flex; align-items: center; height: 14px; margin-top: -7px; }
  .strength__foot::before, .strength__foot::after { content: ""; flex: 1; height: 1px; background: var(--rule); }
  .strength__foot::before { margin-right: 2px; }
  .strength__foot::after { margin-left: 2px; }
  .strength__grade {
    font-family: "Open Sans", sans-serif; font-weight: 600; font-size: 12.5px;
    color: var(--gold); line-height: 1; white-space: nowrap;
  }
  .strength--compact { width: 139px; }
  .strength--compact .strength__frame { height: 53px; padding-top: 3px; }
  .strength--compact .strength__title { font-size: 27px; }
  .strength--compact .strength__dose { font-size: 12px; }
  .strength--compact .strength__grade { font-size: 11px; }

  .flavour {
    position: absolute; left: 0; width: 100%; text-align: center;
    font-family: "Yellowtail", cursive; font-size: 25px; line-height: 1;
    color: var(--script-grey); white-space: nowrap;
    transform: rotate(-9deg);
  }

  .tagline {
    position: absolute; left: 0; width: 100%; text-align: center;
    font-family: "Arimo", sans-serif; font-weight: 700; line-height: 1.3; white-space: nowrap;
  }
  .tagline__line1 { color: var(--tag-deep); font-size: 10px; }
  .tagline__line2 { color: var(--tag-light); font-size: 11px; letter-spacing: 0.3px; }

  .info-box { position: absolute; left: 13.3px; width: 155.2px; }
  .info-box--facts { top: 14.5px; height: 60px; border: 1.2px solid var(--rule); }
  .info-box--ingredients { top: 130.5px; height: 97px; border: 1px solid var(--frame-grey); }

  .label {
    position: absolute; left: 0; top: 867px; width: 1026px; height: 333px;
    background: var(--ink); border-top: 1px solid var(--dieline);
  }
  .label__facts {
    position: absolute; left: 42px; top: 52px; width: 275px; height: 81px;
    border: 1.2px solid var(--rule); border-radius: 14px;
  }
  .label__directions {
    position: absolute; left: 42px; top: 149px; width: 275px; height: 134px;
    background: var(--white); border-radius: 14px;
  }
  .label__center { position: absolute; left: 413px; width: 200px; top: 0; height: 100%; }
  .label__center .brand { top: 35px; }
  .label__rule { position: absolute; left: 740px; width: 244px; height: 1.2px; background: var(--rule); }
  .crop { position: absolute; }
</style>
</head>
<body>
<main class="canvas">

  <svg class="dieline" viewBox="0 0 1026 1200" aria-hidden="true">
    <polygon points="374,1 524,1 540,72 358,72" fill="#fff" stroke="#111" stroke-width="1"/>
    <polygon points="175,255.5 119,283 119,533 175,560" fill="#fff" stroke="#111" stroke-width="1"/>
    <polygon points="540.5,744 557,816 707,816 723.5,744" fill="#fff" stroke="#111" stroke-width="1"/>
  </svg>

  <!-- Top lid -->
  <section class="panel panel--top">
    <div class="brand brand--white" style="top:22px">
      <span class="brand__circle"></span>
      <span class="brand__name">CALM HARBOR CBD</span>
    </div>
    <div class="strength strength--compact" style="top:104px">
      <div class="strength__frame">
        <div class="strength__title">CBD OIL</div>
        <div class="strength__dose">300 mg</div>
      </div>
      <div class="strength__foot"><span class="strength__grade">REGULAR STRENGTH</span></div>
    </div>
  </section>

  <!-- Front panel -->
  <section class="panel panel--front">
    <div class="brand-band">
      <div class="brand brand--navy">
        <span class="brand__circle"></span>
        <span class="brand__name">CALM HARBOR CBD</span>
      </div>
    </div>
    <div class="strength" style="top:121px">
      <div class="strength__frame">
        <div class="strength__title">CBD OIL</div>
        <div class="strength__dose">300 mg</div>
      </div>
      <div class="strength__foot"><span class="strength__grade">REGULAR STRENGTH</span></div>
    </div>
    <div class="flavour" style="top:212px">Natural Flavour</div>
    <div class="tagline" style="top:265px">
      <div class="tagline__line1">RESTORE TO THE BALANCE</div>
      <div class="tagline__line2">TO THE BODY &amp; SOUL</div>
    </div>
  </section>

  <!-- Facts panel -->
  <section class="panel panel--back">
    <div class="info-box info-box--facts"></div>
    <div class="info-box info-box--ingredients"></div>
    <div class="tagline" style="top:265px">
      <div class="tagline__line1">RESTORE TO THE BALANCE</div>
      <div class="tagline__line2">TO THE BODY &amp; SOUL</div>
    </div>
  </section>

  <!-- Second front panel -->
  <section class="panel panel--front-b">
    <div class="brand-band">
      <div class="brand brand--navy">
        <span class="brand__circle"></span>
        <span class="brand__name">CALM HARBOR CBD</span>
      </div>
    </div>
    <div class="strength" style="top:121px">
      <div class="strength__frame">
        <div class="strength__title">CBD OIL</div>
        <div class="strength__dose">300 mg</div>
      </div>
      <div class="strength__foot"><span class="strength__grade">REGULAR STRENGTH</span></div>
    </div>
    <div class="flavour" style="top:212px">Natural Flavour</div>
    <div class="tagline" style="top:265px">
      <div class="tagline__line1">RESTORE TO THE BALANCE</div>
      <div class="tagline__line2">TO THE BODY &amp; SOUL</div>
    </div>
  </section>

  <!-- Second facts panel -->
  <section class="panel panel--back-b">
    <div class="info-box info-box--facts"></div>
    <div class="info-box info-box--ingredients"></div>
    <div class="tagline" style="top:265px">
      <div class="tagline__line1">RESTORE TO THE BALANCE</div>
      <div class="tagline__line2">TO THE BODY &amp; SOUL</div>
    </div>
  </section>

  <!-- Bottom lid -->
  <section class="panel panel--bottom"></section>

  <!-- Bottle label -->
  <section class="label">
    <svg class="crop" style="left:0;top:0" width="1026" height="333" viewBox="0 0 1026 333" aria-hidden="true">
      <g fill="none" stroke="#e6f2f8" stroke-width="1.2">
        <polyline points="25,28 42,28 42,11"/>
        <polyline points="1001,28 984,28 984,11"/>
        <polyline points="25,304 42,304 42,321"/>
        <polyline points="1001,304 984,304 984,321"/>
      </g>
    </svg>
    <div class="label__facts"></div>
    <div class="label__directions"></div>
    <div class="label__center">
      <div class="brand brand--blue">
        <span class="brand__circle"></span>
        <span class="brand__name">CALM HARBOR CBD</span>
      </div>
      <div class="strength" style="top:127px">
        <div class="strength__frame">
          <div class="strength__title">CBD OIL</div>
          <div class="strength__dose">300 mg</div>
        </div>
        <div class="strength__foot"><span class="strength__grade">REGULAR STRENGTH</span></div>
      </div>
      <div class="flavour" style="top:230px">Natural Flavour</div>
      <div class="tagline" style="top:281px">
        <div class="tagline__line1">RESTORE TO THE BALANCE</div>
        <div class="tagline__line2">TO THE BODY &amp; SOUL</div>
      </div>
    </div>
    <div class="label__rule" style="top:106px"></div>
    <div class="label__rule" style="top:197px"></div>
    <div class="label__rule" style="top:256px"></div>
  </section>

</main>
</body>
</html>
```